Employee I.D. Card - Badge

We need an employee I.D. card designed. Our employees are going to be wearing these. I would like to have it look nice. Something professional yet cool (not uptight if that makes sense).
Project Scope:
Vertical orientation
Company name ------------- (Bright and Tidy)
Website ------------- (brightandtidymn.example)
Employee Picture
background check image
front and back designed - same design on either side
You can create the card without having the employee images on them.
Here are the dimensions -
2.125 x 3.370 inches
Double sided - same design can be used front and back
Background badge - I would like to add an image that shows that the employee has taken a background check. I've added the press-kit for the company we use. If you have a better idea than incorporating their logo, we can certainly do something different.
Example image-
https://www.findwell-search.example/results?q=background+check+badge&mode=images
The print company will set up the names.
Logo is attached
Also attached are our business cards. You can use this for an idea of brand/company style.
Our website - brightandtidymn.example

```html
<!DOCTYPE html>
<html lang="en">
<head>
<meta charset="utf-8">
<title>Bright and Tidy – Employee ID Badge</title>
<link rel="stylesheet" href="https://fonts.googleapis.com/css2?family=Arimo:wght@400;500&display=swap">
<style>
  :root {
    --backdrop: #939497;
    --card: #ffffff;
    --brand-blue: #1a8fd4;
    --photo-blue: #24a9e1;
    --photo-tint: #d6eefa;
    --label-lime: #d5e052;
    --slot-grey: #9a9a9a;
    --web-grey: #777777;
    --seal-gold: #d9b54a;
    --seal-dark: #2a2a2a;
    --ink: #111111;
  }
  * { margin: 0; padding: 0; box-sizing: border-box; }
  html, body {
    width: 1200px;
    height: 1200px;
    overflow: hidden;
    background: var(--backdrop);
    font-family: "Arimo", Arial, sans-serif;
  }
  .badge-card {
    position: absolute;
    left: 260px;
    top: 61px;
    width: 680px;
    height: 1078px;
    background: var(--card);
    border-radius: 9px;
    overflow: hidden;
  }
  .lanyard-slot {
    position: absolute;
    left: 236px;
    top: 34px;
    width: 188px;
    height: 22px;
    border-radius: 11px;
    background: var(--slot-grey);
  }
  .company-name {
    position: absolute;
    left: 0;
    width: 100%;
    top: 150px;
    text-align: center;
    font-size: 66px;
    font-weight: 400;
    letter-spacing: -1px;
    color: var(--brand-blue);
  }
  .company-website {
    position: absolute;
    left: 0;
    width: 100%;
    top: 303px;
    text-align: center;
    font-size: 24px;
    color: var(--web-grey);
  }
  .photo-frame {
    position: absolute;
    left: 0;
    top: 0;
  }
  .name-plate {
    position: absolute;
    left: 118px;
    top: 911px;
    width: 445px;
    height: 167px;
    background: var(--label-lime);
    text-align: center;
    padding-top: 23px;
    font-size: 39px;
    line-height: 47px;
    color: var(--ink);
  }
</style>
</head>
<body>
  <main class="badge-card">
    <div class="lanyard-slot"></div>

    <h1 class="company-name">Bright and Tidy</h1>
    <p class="company-website">www.brightandtidymn.example</p>

    <svg class="photo-frame" width="680" height="1078" viewBox="0 0 680 1078">
      <defs>
        <radialGradient id="photo-fill" cx="50%" cy="35%" r="70%">
          <stop offset="0%" stop-color="var(--photo-tint)"/>
          <stop offset="100%" stop-color="var(--photo-blue)"/>
        </radialGradient>
      </defs>
      <g class="employee-photo" role="img" aria-label="Employee photo placeholder">
        <circle cx="357" cy="610" r="246" fill="url(#photo-fill)"/>
      </g>
      <circle class="photo-ring" cx="357" cy="610" r="252" fill="none" stroke="var(--photo-blue)" stroke-width="6"/>
      <g class="background-check-seal" role="img" aria-label="Background check cleared seal">
        <circle cx="542" cy="800" r="99" fill="var(--seal-gold)"/>
        <circle cx="542" cy="800" r="82" fill="var(--seal-dark)"/>
        <circle cx="542" cy="800" r="40" fill="var(--seal-gold)"/>
      </g>
    </svg>

    <div class="name-plate">
      <div class="name-line">NAME</div>
      <div class="designation-line">DESIGNATION</div>
    </div>
  </main>
</body>
</html>
```